Point of sale box designs , I have templets.

I need point of sale box design according to my requirements.
I have all files at the ready. Each windows file has a;; the information you will need.
see files I uploded.
This project is 90% cut and paste. look into all the windows files for instructions ,text, bar codes and there placement.
You only have to draw the 3 steps on how to use the product.
Industry/Entity Type
General consumer product.
Nice to have
- Taxi cab yellow background with black text.

```html
<!DOCTYPE html>
<html lang="en">
<head>
<meta charset="utf-8">
<title>The Sachet Punch – Point of Sale Packaging</title>
<link href="https://fonts.googleapis.com/css2?family=Catamaran:wght@300;400;600;700&family=Montserrat:wght@900&display=swap" rel="stylesheet">
<style>
  :root {
    --taxi-yellow: #fbb91e;
    --ink: #111111;
    --paper: #ffffff;
    --cut-line: #4b49a8;
    --fold-line: #c07f12;
    --tab-brown: #97825a;
    --art-tint: #fcd37a;
  }
  html, body {
    margin: 0;
    padding: 0;
    width: 971px;
    height: 1200px;
    overflow: hidden;
    background: var(--paper);
  }
  .sheet { display: block; width: 971px; height: 1200px; }
  .body-text { font-family: "Catamaran", sans-serif; fill: var(--ink); }
  .headline { font-family: "Montserrat", sans-serif; font-weight: 900; fill: var(--ink); }
  .bold { font-weight: 700; }
  .semi { font-weight: 600; }
  .light { font-weight: 300; }
  .white-text { fill: var(--paper); }
  .panel { fill: var(--taxi-yellow); }
  .cut { fill: none; stroke: var(--cut-line); stroke-width: 1.2; }
  .cut-fill { fill: var(--paper); stroke: var(--cut-line); stroke-width: 1.2; }
  .fold { stroke: var(--fold-line); stroke-width: 1; stroke-dasharray: 3 3; fill: none; }
  .dimension { stroke: var(--ink); stroke-width: 2; }
  .dimension-label { font-family: "Catamaran", sans-serif; font-weight: 400; fill: var(--ink); }
  .step-art { fill: var(--paper); }
  .product-art { fill: var(--art-tint); }
  .hang-tab { fill: var(--paper); }
  .tab-shape { fill: var(--tab-brown); }
  .tab-slot { fill: var(--paper); }
  .pill { fill: var(--ink); }
</style>
</head>
<body>
<svg class="sheet" viewBox="0 0 1728 2160" preserveAspectRatio="xMidYMid meet" xmlns="http://www.w3.org/2000/svg">

  <!-- ===== Box dieline ===== -->
  <g class="dieline">
    <!-- tuck flap -->
    <path class="cut" d="M262 327 V165 Q262 151 276 151 H514 Q528 151 528 165 V327"/>

    <!-- lid panel -->
    <rect class="panel" x="258" y="327" width="273" height="363"/>
    <path class="cut" d="M258 327 H531 V690"/>
    <path class="cut" d="M258 327 V690"/>
    <g transform="rotate(180 395 437)">
      <text class="headline" x="395" y="428" font-size="25" text-anchor="middle">THE SACHET</text>
      <text class="headline" x="395" y="456" font-size="25" text-anchor="middle">PUNCH</text>
    </g>
    <rect class="product-art" x="307" y="484" width="165" height="70" rx="34" role="img" aria-label="Outline drawing of the sachet punch tool"/>
    <path class="cut" d="M286 508 A109 106 0 0 0 504 508"/>
    <path class="fold" d="M258 508 H286 M504 508 H531"/>
    <g transform="rotate(180 307 674)">
      <text class="body-text" x="307" y="677" font-size="8" text-anchor="middle">European</text>
    </g>
    <g transform="rotate(180 483 674)">
      <text class="body-text" x="483" y="677" font-size="8" text-anchor="middle">U.S.A &amp; Canada</text>
    </g>

    <!-- glue flap -->
    <path class="panel" d="M214 702 L258 690 V872 L214 860 Z"/>
    <path class="cut" d="M258 690 L214 702 V860 L258 872"/>

    <!-- main band -->
    <rect class="panel" x="258" y="690" width="1276" height="182"/>
    <path class="fold" d="M258 690 H1534 M258 872 H1534 M531 690 V872 M896 690 V872 M1170 690 V872 M260 690 V872"/>
    <path class="cut" d="M1534 690 V872"/>

    <!-- dust flaps top -->
    <path class="cut-fill" d="M536 690 L562 600 H868 L886 668 L892 672 V690"/>
    <path class="cut-fill" d="M1174 690 V672 L1180 668 L1197 600 H1503 L1530 690"/>

    <!-- bottom flaps -->
    <path class="cut-fill" d="M263 872 V1045 H380 Q395 1045 395 1030 V962 L533 872"/>
    <path class="cut-fill" d="M535 872 V1045 H608 Q622 1045 622 1030 V1006 H804 V1030 Q804 1045 818 1045 H892 V872"/>
    <path class="cut-fill" d="M895 872 L1032 962 V1030 Q1032 1045 1047 1045 H1165 V872"/>
    <path class="cut-fill" d="M1168 872 L1260 1008 V1031 Q1260 1045 1275 1045 H1428 Q1442 1045 1442 1031 V1008 L1534 872"/>

    <!-- panel 1: back info -->
    <circle cx="303" cy="733" r="24" fill="var(--paper)"/>
    <text class="body-text semi" x="271" y="832" font-size="9">Dishwasher Safe</text>
    <text class="body-text" x="271" y="844" font-size="9">Not a child’s toy,</text>
    <text class="body-text" x="271" y="855" font-size="9">keep away from small children</text>
    <text class="headline" x="519" y="828" font-size="13" text-anchor="end">Visit Us at:</text>
    <text class="body-text" x="519" y="841" font-size="10.5" text-anchor="end">www.saucepokeco.com</text>
    <text class="body-text semi" x="519" y="856" font-size="9" text-anchor="end">Made in China</text>

    <!-- panel 2: steps -->
    <text class="body-text" x="713" y="721" font-size="11.5" text-anchor="middle">So simple to use even a child can do it.</text>
    <text class="body-text bold" x="610" y="744" font-size="10" text-anchor="middle">Step 1</text>
    <text class="body-text bold" x="713" y="744" font-size="10" text-anchor="middle">Step 2</text>
    <text class="body-text bold" x="817" y="744" font-size="10" text-anchor="middle">Step 3</text>
    <rect class="step-art" x="565" y="751" width="89" height="88" rx="4" role="img" aria-label="Hands shaking a sachet so the contents settle"/>
    <rect class="step-art" x="669" y="751" width="89" height="88" rx="4" role="img" aria-label="Hands piercing the sachet with the tool"/>
    <rect class="step-art" x="773" y="751" width="89" height="88" rx="4" role="img" aria-label="Hand squeezing sauce out of the sachet"/>
    <text class="body-text" x="610" y="856" font-size="7" text-anchor="middle">Shake the contents to the bottom</text>
    <text class="body-text" x="713" y="856" font-size="7" text-anchor="middle">Pierce the packet 3 to 4 times</text>
    <text class="body-text" x="817" y="856" font-size="7" text-anchor="middle">Slowly squeeze the contents out</text>

    <!-- panel 3 -->
    <text class="body-text" x="1033" y="770" font-size="12.5" text-anchor="middle">Don’t put the condiment packet in your</text>
    <text class="body-text" x="1033" y="785" font-size="12.5" text-anchor="middle">mouth to open it. That’s just gross.</text>
    <text class="body-text" x="1033" y="800" font-size="12.5" text-anchor="middle">Use our Sachet Punch.</text>
    <rect class="pill" x="955" y="836" width="155" height="16" rx="8"/>
    <text class="body-text bold white-text" x="1032" y="847" font-size="9.5" text-anchor="middle">For people on the go</text>

    <!-- panel 4 -->
    <g class="body-text" font-size="11">
      <text x="1188" y="724">Designed with precision and ease in mind, our Sachet Punch</text>
      <text x="1188" y="740">will effortlessly puncture through those tough foil or plastic</text>
      <text x="1188" y="756">sachets, allowing you to conveniently release the perfect amount of</text>
      <text x="1188" y="772">sauce onto your food. No more struggling, no more spills - just pure</text>
      <text x="1188" y="788">flavor, unleashed!</text>
    </g>
    <rect class="product-art" x="1342" y="790" width="166" height="70" rx="34" role="img" aria-label="Outline drawing of the sachet punch tool"/>
  </g>

  <!-- box dimensions -->
  <line class="dimension" x1="1602" y1="151" x2="1602" y2="1045"/>
  <text class="dimension-label" x="1512" y="485" font-size="28" text-anchor="middle">490.5 mm</text>
  <line class="dimension" x1="214" y1="1111" x2="1534" y2="1111"/>
  <text class="dimension-label" x="878" y="1176" font-size="28" text-anchor="middle">724 mm</text>

  <!-- ===== Hang card: front ===== -->
  <g class="card-front">
    <rect class="panel" x="406" y="1320" width="370" height="586" rx="18"/>
    <circle class="hang-tab" cx="591" cy="1343" r="12"/>
    <rect class="hang-tab" x="499" y="1347" width="184" height="25" rx="5"/>
    <rect class="product-art" x="460" y="1385" width="235" height="92" rx="46" opacity="0.7" role="img" aria-label="Outline drawing of the sachet punch tool behind the title"/>
    <text class="headline" x="592" y="1430" font-size="31" text-anchor="middle">THE SACHET</text>
    <text class="headline" x="592" y="1461" font-size="31" text-anchor="middle">PUNCH</text>

    <g class="tabs-left">
      <path class="tab-shape" d="M406 1500 H560 A31 31 0 0 1 560 1562 H406 Z"/>
      <rect class="tab-slot" x="406" y="1526" width="65" height="10" rx="5"/>
      <path class="tab-shape" d="M406 1589 H560 A31 31 0 0 1 560 1651 H406 Z"/>
      <rect class="tab-slot" x="406" y="1615" width="65" height="10" rx="5"/>
      <path class="tab-shape" d="M406 1677 H560 A31 31 0 0 1 560 1739 H406 Z"/>
      <rect class="tab-slot" x="406" y="1703" width="65" height="10" rx="5"/>
      <path class="tab-shape" d="M406 1766 H560 A31 31 0 0 1 560 1828 H406 Z"/>
      <rect class="tab-slot" x="406" y="1792" width="65" height="10" rx="5"/>
    </g>

    <text class="body-text" x="689" y="1519" font-size="14.5" text-anchor="middle">Inventory Barcodes:</text>
    <text class="body-text" x="689" y="1634" font-size="14.5" text-anchor="middle">U.S.A &amp; Canada</text>
    <text class="body-text" x="689" y="1751" font-size="13" text-anchor="middle">EU</text>

    <text class="headline" x="751" y="1833" font-size="17" text-anchor="end">Visit Us at:</text>
    <text class="body-text" x="751" y="1852" font-size="17" text-anchor="end">www.saucepokeco.com</text>
    <text class="body-text" x="751" y="1870" font-size="11.5" text-anchor="end">Copyright &amp; Trademarked</text>
    <text class="body-text semi" x="751" y="1887" font-size="13.5" text-anchor="end">Not a child’s toy, keep away from small children</text>
  </g>

  <!-- card dimensions -->
  <line class="dimension" x1="365" y1="1320" x2="365" y2="1904"/>
  <text class="dimension-label" x="277" y="1613" font-size="26" text-anchor="middle">9.5 inch</text>
  <line class="dimension" x1="406" y1="1942" x2="776" y2="1942"/>
  <text class="dimension-label" x="576" y="1993" font-size="26" text-anchor="middle">6 inch</text>

  <!-- ===== Hang card: back ===== -->
  <g class="card-back">
    <rect class="panel" x="992" y="1320" width="370" height="586" rx="18"/>
    <circle class="hang-tab" cx="1177" cy="1343" r="12"/>
    <rect class="hang-tab" x="1085" y="1347" width="184" height="25" rx="5"/>

    <text class="body-text semi" x="1091" y="1492" font-size="14.5" text-anchor="middle">U.S.A &amp; Canada</text>
    <text class="body-text semi" x="1263" y="1492" font-size="14.5" text-anchor="middle">EU</text>

    <rect class="product-art" x="1036" y="1522" width="98" height="210" rx="49" opacity="0.7" role="img" aria-label="Outline drawing of the sachet punch tool, standing upright"/>

    <g class="tabs-right">
      <path class="tab-shape" d="M1362 1500 H1208 A31 31 0 0 0 1208 1562 H1362 Z"/>
      <rect class="tab-slot" x="1297" y="1526" width="65" height="10" rx="5"/>
      <path class="tab-shape" d="M1362 1589 H1208 A31 31 0 0 0 1208 1651 H1362 Z"/>
      <rect class="tab-slot" x="1297" y="1615" width="65" height="10" rx="5"/>
      <path class="tab-shape" d="M1362 1677 H1208 A31 31 0 0 0 1208 1739 H1362 Z"/>
      <rect class="tab-slot" x="1297" y="1703" width="65" height="10" rx="5"/>
      <path class="tab-shape" d="M1362 1766 H1208 A31 31 0 0 0 1208 1828 H1362 Z"/>
      <rect class="tab-slot" x="1297" y="1792" width="65" height="10" rx="5"/>
    </g>

    <g class="body-text" font-size="15.5">
      <text x="1019" y="1634">So simple to use even</text>
      <text x="1019" y="1653">a child can do it.</text>
      <text x="1019" y="1681">Don’t put the condi</text>
      <text x="1019" y="1700">ment packet in your</text>
      <text x="1019" y="1719">mouth to open it.</text>
      <text x="1019" y="1758">That’s just gross.</text>
      <text x="1019" y="1807">Use our Sachet</text>
      <text x="1019" y="1826">Punch.</text>
    </g>
    <text class="body-text semi" x="1021" y="1881" font-size="14.5">Made in China</text>
    <text class="body-text semi" x="1333" y="1881" font-size="14.5" text-anchor="end">Dishwasher Safe</text>
  </g>
</svg>
</body>
</html>
```